Step and Repeat Backdrop for wedding reception photo booth

Would like to have a Step and Repeat Backdrop (8 foot high by 10 foot wide) that incorporates the wedding logo (attached) and the names Elena and Gavin. Background should be white, and wedding colors are burgundy and gold. Show me creativity :-) I have included some random samples.

```html
<!DOCTYPE html>
<html lang="en">
<head>
<meta charset="utf-8">
<title>Elena &amp; Gavin — Step and Repeat Backdrop</title>
<link rel="stylesheet" href="https://fonts.googleapis.com/css2?family=Cinzel:wght@600&family=Josefin+Sans:wght@400&display=swap">
<style>
  :root {
    --page-bg: #e6e6e6;
    --backdrop-white: #ffffff;
    --burgundy: #7e0c19;
    --gold: #b48a3c;
    --gold-light: #d9b867;
    --gold-soft: rgba(196, 156, 76, 0.55);
  }
  * { box-sizing: border-box; margin: 0; padding: 0; }
  html, body {
    width: 1200px;
    height: 1200px;
    overflow: hidden;
    background: var(--page-bg);
  }
  .backdrop {
    position: absolute;
    left: 20px;
    top: 150px;
    width: 1160px;
    height: 900px;
    background: var(--backdrop-white);
    overflow: hidden;
  }
  .repeat-grid {
    position: absolute;
    left: -6px;
    top: -14px;
    display: grid;
    grid-template-columns: repeat(9, 131px);
    grid-template-rows: repeat(5, 186px);
  }
  .tile {
    display: flex;
    flex-direction: column;
    align-items: center;
    justify-content: center;
    gap: 6px;
  }
  .flourish {
    display: block;
    width: 86px;
    height: 9px;
    border-radius: 5px;
    background: linear-gradient(90deg, transparent, var(--gold-soft) 20%, var(--gold-soft) 80%, transparent);
  }
  .tile-square {
    width: 109px;
    height: 109px;
    border-radius: 4px;
    background: var(--burgundy);
    display: flex;
    align-items: center;
    justify-content: center;
  }
  .tile-name {
    font-family: "Cinzel", serif;
    font-weight: 600;
    font-size: 15px;
    line-height: 1.25;
    color: var(--gold);
    text-align: center;
    letter-spacing: 0.5px;
  }
  .tile--burgundy .tile-name { color: var(--gold-light); }
  .tile--white .tile-name { font-size: 16px; }
  .feature {
    grid-row: 3;
    grid-column: 4 / span 3;
    display: flex;
    flex-direction: column;
    align-items: center;
    justify-content: center;
    gap: 14px;
  }
  .feature-flourish {
    display: block;
    width: 236px;
    height: 30px;
    border-radius: 15px;
    background: linear-gradient(90deg, transparent, var(--gold-soft) 18%, var(--gold-soft) 82%, transparent);
  }
  .feature-name {
    font-family: "Cinzel", serif;
    font-weight: 600;
    font-size: 44px;
    line-height: 1.05;
    color: var(--gold);
    text-align: center;
  }
</style>
</head>
<body>
  <main class="backdrop">
    <div class="repeat-grid">
      <section class="feature">
        <span class="feature-flourish" role="img" aria-label="Gold scroll flourish above the couple's names"></span>
        <h1 class="feature-name">Elena<br>&amp; Gavin</h1>
        <span class="feature-flourish" role="img" aria-label="Gold scroll flourish below the couple's names"></span>
      </section>

      <!-- row 1 -->
      <div class="tile tile--white"><span class="flourish" role="img" aria-label="Gold flourish"></span><span class="tile-name">Elena<br>&amp; Gavin</span><span class="flourish" role="img" aria-label="Gold flourish"></span></div>
      <div class="tile tile--burgundy"><span class="flourish" role="img" aria-label="Gold crown flourish"></span><div class="tile-square"><span class="tile-name">Elena<br>&amp; Gavin</span></div><span class="flourish" role="img" aria-label="Gold flourish"></span></div>
      <div class="tile tile--white"><span class="flourish" role="img" aria-label="Gold flourish"></span><span class="tile-name">Elena<br>&amp; Gavin</span><span class="flourish" role="img" aria-label="Gold flourish"></span></div>
      <div class="tile tile--burgundy"><span class="flourish" role="img" aria-label="Gold crown flourish"></span><div class="tile-square"><span class="tile-name">Elena<br>&amp; Gavin</span></div><span class="flourish" role="img" aria-label="Gold flourish"></span></div>
      <div class="tile tile--white"><span class="flourish" role="img" aria-label="Gold flourish"></span><span class="tile-name">Elena<br>&amp; Gavin</span><span class="flourish" role="img" aria-label="Gold flourish"></span></div>
      <div class="tile tile--burgundy"><span class="flourish" role="img" aria-label="Gold crown flourish"></span><div class="tile-square"><span class="tile-name">Elena<br>&amp; Gavin</span></div><span class="flourish" role="img" aria-label="Gold flourish"></span></div>
      <div class="tile tile--white"><span class="flourish" role="img" aria-label="Gold flourish"></span><span class="tile-name">Elena<br>&amp; Gavin</span><span class="flourish" role="img" aria-label="Gold flourish"></span></div>
      <div class="tile tile--burgundy"><span class="flourish" role="img" aria-label="Gold crown flourish"></span><div class="tile-square"><span class="tile-name">Elena<br>&amp; Gavin</span></div><span class="flourish" role="img" aria-label="Gold flourish"></span></div>
      <div class="tile tile--white"><span class="flourish" role="img" aria-label="Gold flourish"></span><span class="tile-name">Elena<br>&amp; Gavin</span><span class="flourish" role="img" aria-label="Gold flourish"></span></div>

      <!-- row 2 -->
      <div class="tile tile--burgundy"><span class="flourish" role="img" aria-label="Gold crown flourish"></span><div class="tile-square"><span class="tile-name">Elena<br>&amp; Gavin</span></div><span class="flourish" role="img" aria-label="Gold flourish"></span></div>
      <div class="tile tile--white"><span class="flourish" role="img" aria-label="Gold flourish"></span><span class="tile-name">Elena<br>&amp; Gavin</span><span class="flourish" role="img" aria-label="Gold flourish"></span></div>
      <div class="tile tile--burgundy"><span class="flourish" role="img" aria-label="Gold crown flourish"></span><div class="tile-square"><span class="tile-name">Elena<br>&amp; Gavin</span></div><span class="flourish" role="img" aria-label="Gold flourish"></span></div>
      <div class="tile tile--white"><span class="flourish" role="img" aria-label="Gold flourish"></span><span class="tile-name">Elena<br>&amp; Gavin</span><span class="flourish" role="img" aria-label="Gold flourish"></span></div>
      <div class="tile tile--burgundy"><span class="flourish" role="img" aria-label="Gold crown flourish"></span><div class="tile-square"><span class="tile-name">Elena<br>&amp; Gavin</span></div><span class="flourish" role="img" aria-label="Gold flourish"></span></div>
      <div class="tile tile--white"><span class="flourish" role="img" aria-label="Gold flourish"></span><span class="tile-name">Elena<br>&amp; Gavin</span><span class="flourish" role="img" aria-label="Gold flourish"></span></div>
      <div class="tile tile--burgundy"><span class="flourish" role="img" aria-label="Gold crown flourish"></span><div class="tile-square"><span class="tile-name">Elena<br>&amp; Gavin</span></div><span class="flourish" role="img" aria-label="Gold flourish"></span></div>
      <div class="tile tile--white"><span class="flourish" role="img" aria-label="Gold flourish"></span><span class="tile-name">Elena<br>&amp; Gavin</span><span class="flourish" role="img" aria-label="Gold flourish"></span></div>
      <div class="tile tile--burgundy"><span class="flourish" role="img" aria-label="Gold crown flourish"></span><div class="tile-square"><span class="tile-name">Elena<br>&amp; Gavin</span></div><span class="flourish" role="img" aria-label="Gold flourish"></span></div>

      <!-- row 3 (centre reserved for feature) -->
      <div class="tile tile--white"><span class="flourish" role="img" aria-label="Gold flourish"></span><span class="tile-name">Elena<br>&amp; Gavin</span><span class="flourish" role="img" aria-label="Gold flourish"></span></div>
      <div class="tile tile--burgundy"><span class="flourish" role="img" aria-label="Gold crown flourish"></span><div class="tile-square"><span class="tile-name">Elena<br>&amp; Gavin</span></div><span class="flourish" role="img" aria-label="Gold flourish"></span></div>
      <div class="tile tile--white"><span class="flourish" role="img" aria-label="Gold flourish"></span><span class="tile-name">Elena<br>&amp; Gavin</span><span class="flourish" role="img" aria-label="Gold flourish"></span></div>
      <div class="tile tile--white"><span class="flourish" role="img" aria-label="Gold flourish"></span><span class="tile-name">Elena<br>&amp; Gavin</span><span class="flourish" role="img" aria-label="Gold flourish"></span></div>
      <div class="tile tile--burgundy"><span class="flourish" role="img" aria-label="Gold crown flourish"></span><div class="tile-square"><span class="tile-name">Elena<br>&amp; Gavin</span></div><span class="flourish" role="img" aria-label="Gold flourish"></span></div>
      <div class="tile tile--white"><span class="flourish" role="img" aria-label="Gold flourish"></span><span class="tile-name">Elena<br>&amp; Gavin</span><span class="flourish" role="img" aria-label="Gold flourish"></span></div>

      <!-- row 4 -->
      <div class="tile tile--burgundy"><span class="flourish" role="img" aria-label="Gold crown flourish"></span><div class="tile-square"><span class="tile-name">Elena<br>&amp; Gavin</span></div><span class="flourish" role="img" aria-label="Gold flourish"></span></div>
      <div class="tile tile--white"><span class="flourish" role="img" aria-label="Gold flourish"></span><span class="tile-name">Elena<br>&amp; Gavin</span><span class="flourish" role="img" aria-label="Gold flourish"></span></div>
      <div class="tile tile--burgundy"><span class="flourish" role="img" aria-label="Gold crown flourish"></span><div class="tile-square"><span class="tile-name">Elena<br>&amp; Gavin</span></div><span class="flourish" role="img" aria-label="Gold flourish"></span></div>
      <div class="tile tile--white"><span class="flourish" role="img" aria-label="Gold flourish"></span><span class="tile-name">Elena<br>&amp; Gavin</span><span class="flourish" role="img" aria-label="Gold flourish"></span></div>
      <div class="tile tile--burgundy"><span class="flourish" role="img" aria-label="Gold crown flourish"></span><div class="tile-square"><span class="tile-name">Elena<br>&amp; Gavin</span></div><span class="flourish" role="img" aria-label="Gold flourish"></span></div>
      <div class="tile tile--white"><span class="flourish" role="img" aria-label="Gold flourish"></span><span class="tile-name">Elena<br>&amp; Gavin</span><span class="flourish" role="img" aria-label="Gold flourish"></span></div>
      <div class="tile tile--burgundy"><span class="flourish" role="img" aria-label="Gold crown flourish"></span><div class="tile-square"><span class="tile-name">Elena<br>&amp; Gavin</span></div><span class="flourish" role="img" aria-label="Gold flourish"></span></div>
      <div class="tile tile--white"><span class="flourish" role="img" aria-label="Gold flourish"></span><span class="tile-name">Elena<br>&amp; Gavin</span><span class="flourish" role="img" aria-label="Gold flourish"></span></div>
      <div class="tile tile--burgundy"><span class="flourish" role="img" aria-label="Gold crown flourish"></span><div class="tile-square"><span class="tile-name">Elena<br>&amp; Gavin</span></div><span class="flourish" role="img" aria-label="Gold flourish"></span></div>

      <!-- row 5 -->
      <div class="tile tile--white"><span class="flourish" role="img" aria-label="Gold flourish"></span><span class="tile-name">Elena<br>&amp; Gavin</span><span class="flourish" role="img" aria-label="Gold flourish"></span></div>
      <div class="tile tile--burgundy"><span class="flourish" role="img" aria-label="Gold crown flourish"></span><div class="tile-square"><span class="tile-name">Elena<br>&amp; Gavin</span></div><span class="flourish" role="img" aria-label="Gold flourish"></span></div>
      <div class="tile tile--white"><span class="flourish" role="img" aria-label="Gold flourish"></span><span class="tile-name">Elena<br>&amp; Gavin</span><span class="flourish" role="img" aria-label="Gold flourish"></span></div>
      <div class="tile tile--burgundy"><span class="flourish" role="img" aria-label="Gold crown flourish"></span><div class="tile-square"><span class="tile-name">Elena<br>&amp; Gavin</span></div><span class="flourish" role="img" aria-label="Gold flourish"></span></div>
      <div class="tile tile--white"><span class="flourish" role="img" aria-label="Gold flourish"></span><span class="tile-name">Elena<br>&amp; Gavin</span><span class="flourish" role="img" aria-label="Gold flourish"></span></div>
      <div class="tile tile--burgundy"><span class="flourish" role="img" aria-label="Gold crown flourish"></span><div class="tile-square"><span class="tile-name">Elena<br>&amp; Gavin</span></div><span class="flourish" role="img" aria-label="Gold flourish"></span></div>
      <div class="tile tile--white"><span class="flourish" role="img" aria-label="Gold flourish"></span><span class="tile-name">Elena<br>&amp; Gavin</span><span class="flourish" role="img" aria-label="Gold flourish"></span></div>
      <div class="tile tile--burgundy"><span class="flourish" role="img" aria-label="Gold crown flourish"></span><div class="tile-square"><span class="tile-name">Elena<br>&amp; Gavin</span></div><span class="flourish" role="img" aria-label="Gold flourish"></span></div>
      <div class="tile tile--white"><span class="flourish" role="img" aria-label="Gold flourish"></span><span class="tile-name">Elena<br>&amp; Gavin</span><span class="flourish" role="img" aria-label="Gold flourish"></span></div>
    </div>
  </main>
</body>
</html>
```